Startup but Passionate F&B Company with big dreams for the future and multiple brands needs business

We need a simple logo and typography design for business card usage for a new company in a bustling and modern city called Brindle Terrace Pte Ltd. We are an F&B company that owns multiple brands of small boutique and indie cafes and eateries. We offer artisanal and home made food created with passion using quality and fresh ingredient. We would like to remain relevant and grow in the future constantly adapting changes and testing new boundaries with our menu and offerings in line with moving tastes and times. Final design and colors should be simple, fresh but modern and will remain relevant in time to come. For fonts we prefer modern fonts such as avenir (meaning future/futuristic) or any other new and trendy font types.
Updates

Please include a logo design as well as typography on th name card.

Thanks

Industry/Entity Type

Boutique

Font styles to use
Other font styles liked:
• Avenir or any other modern looking fonts

Colors

Designer to choose colors to be used in the design.

Requirements
Must have
• Logo + typography

```html
<!DOCTYPE html>
<html lang="en">
<head>
<meta charset="utf-8">
<title>Brindle Terrace Pte Ltd — Business Card</title>
<link rel="stylesheet" href="https://fonts.googleapis.com/css2?family=Ubuntu:wght@400;500;700&display=swap">
<style>
  :root {
    --backdrop: #161616;
    --paper: #f2f2ef;
    --paper-shade: #e6e6e2;
    --ink: #1a1a1a;
    --card-dark: #1c1c1c;
    --accent: #4cc43a;
    --accent-light: #6ee05a;
    --light-text: #f4f4f4;
  }
  * { margin: 0; padding: 0; box-sizing: border-box; }
  html, body {
    width: 1050px;
    height: 1200px;
    overflow: hidden;
    background: var(--backdrop);
    font-family: "Ubuntu", sans-serif;
  }
  .stage {
    width: 1050px;
    height: 1200px;
    display: flex;
    align-items: center;
    justify-content: center;
  }
  .business-card {
    position: relative;
    width: 900px;
    height: 512px;
    background: var(--card-dark);
    overflow: hidden;
  }
  .card-top {
    position: absolute;
    left: 0; top: 0;
    width: 100%;
    height: 270px;
    background: radial-gradient(ellipse at 60% 40%, var(--paper) 0%, var(--paper-shade) 100%);
  }
  .accent-rule {
    position: absolute;
    left: 0; top: 270px;
    width: 100%;
    height: 8px;
    background: linear-gradient(var(--accent-light), var(--accent));
  }
  .brand {
    position: absolute;
    left: 48px;
    top: 53px;
    display: flex;
    align-items: center;
    gap: 16px;
  }
  .brand-square {
    width: 80px;
    height: 80px;
    background: var(--accent);
  }
  .brand-name {
    color: var(--ink);
    font-weight: 700;
    font-size: 27px;
    line-height: 1.15;
  }
  .person {
    position: absolute;
    right: 53px;
    top: 58px;
    text-align: right;
  }
  .person-name {
    color: var(--ink);
    font-weight: 400;
    font-size: 39px;
    line-height: 1.1;
  }
  .person-title {
    color: var(--accent);
    font-weight: 400;
    font-size: 29px;
    line-height: 1.1;
  }
  .contact-list {
    position: absolute;
    right: 53px;
    top: 392px;
    list-style: none;
    text-align: right;
    font-size: 20px;
    line-height: 30px;
    color: var(--light-text);
  }
  .label { color: var(--accent-light); }
  .web {
    position: absolute;
    left: 40px;
    top: 452px;
    font-size: 20px;
    line-height: 30px;
    color: var(--light-text);
  }
</style>
</head>
<body>
  <main class="stage">
    <article class="business-card">
      <div class="card-top"></div>
      <div class="accent-rule"></div>

      <div class="brand">
        <div class="brand-square"></div>
        <div class="brand-name">Brindle Terrace<br>Pte Ltd.</div>
      </div>

      <div class="person">
        <div class="person-name">Mara Quill</div>
        <div class="person-title">CEO</div>
      </div>

      <ul class="contact-list">
        <li><span class="label">mobile:</span> +123 555 018</li>
        <li><span class="label">phone/fax:</span> +123 555 018</li>
        <li><span class="label">email:</span> info@brindleterrace.com</li>
      </ul>

      <div class="web"><span class="label">web:</span> www.brindleterrace.com</div>
    </article>
  </main>
</body>
</html>
```